Digital One Pager for Consulting Practice

I would like the essence of the content in my ppt consolidated into a one-pager. The one-pager will mainly be sent via email as a pdf and intended to excite and invite new clients and establish the credibility of my boutique high-end consulting firm. Infographics and symbols would be a plus. The target client should view the firm as providing premeir service. The client is getting a thought partner.

Target Market(s)

Large Medical Device Manufacturer Executives, Early-Stage Medical Device Manufacturer Executives, Partners at VC Firms

Industry/Entity Type

Medical Equipment

Colors
0355a3
f37122

Requirements
Must have
• Please match the color scheme in ppt. Please use the existing logo. I am very open to better graphics on the process. My photo does not need to be on the digital flyer. Hyper link to the website and email is needed.
Nice to have
• Infographics

```html
<!DOCTYPE html>
<html lang="en">
<head>
<meta charset="utf-8">
<title>Halden Advisory – One Pager</title>
<link href="https://fonts.googleapis.com/css2?family=Tinos:ital,wght@0,400;0,700;1,400&family=Lato:wght@400;700&family=Roboto:wght@500&display=swap" rel="stylesheet">
<style>
  :root{
    --navy:#0f1b3d;
    --orange:#f37122;
    --blue:#0355a3;
    --blue-light:#3f72c6;
    --blue-mid:#2f63bb;
    --blue-deep:#1f4fb2;
    --white:#ffffff;
    --ink:#1b1f2a;
    --page:#e6e7ea;
    --venn-edge:#8fd3a9;
  }
  *{box-sizing:border-box;margin:0;padding:0}
  html,body{width:1188px;height:1200px;overflow:hidden;background:var(--page)}
  .flyer{position:absolute;left:138px;top:10px;width:912px;height:1180px;background:var(--white);overflow:hidden;font-family:"Lato",Arial,sans-serif;color:var(--ink)}

  /* header */
  .hero{position:absolute;left:0;top:0;width:912px;height:250px}
  .hero svg{position:absolute;inset:0}
  .hero h1{position:absolute;left:0;right:0;top:58px;text-align:center;font-family:"Tinos","Times New Roman",serif;font-weight:400;font-size:50px;line-height:58px;color:var(--white)}

  /* experience */
  .experience{position:absolute;left:60px;top:258px;width:470px}
  .section-title{font-family:"Tinos","Times New Roman",serif;font-weight:700;font-size:28px;letter-spacing:.5px}
  .bullets{list-style:none;margin-top:14px}
  .bullets li{position:relative;padding-left:22px;font-size:14.5px;line-height:19px;margin-bottom:10px}
  .bullets li::before{content:"";position:absolute;left:2px;top:6px;width:8px;height:8px;border-radius:50%;background:var(--orange)}
  .bullets li.tight{margin-bottom:1px}
  .bullets li.gap{margin-top:18px}

  .venn{position:absolute;left:548px;top:240px;width:340px;height:300px}
  .venn text{font-family:"Tinos",serif;font-style:italic;font-size:13px;fill:var(--white);text-decoration:underline;text-anchor:middle}

  /* split row */
  .services{position:absolute;left:0;top:562px;width:470px;height:290px;background:var(--orange);color:var(--white);padding:24px 30px 0 48px}
  .services .section-title{font-size:27px}
  .svc-cols{display:flex;gap:28px;margin-top:6px}
  .svc-col{flex:1}
  .svc-head{font-family:"Tinos",serif;font-weight:700;font-size:17px;color:var(--navy);margin:10px 0 6px}
  .svc-list{list-style:none}
  .svc-list li{position:relative;padding-left:14px;font-size:13px;line-height:17px;margin-bottom:10px}
  .svc-list li::before{content:"";position:absolute;left:0;top:6px;width:6px;height:6px;border-radius:50%;background:var(--white)}

  .provide{position:absolute;left:470px;top:562px;width:442px;height:290px;background:var(--navy);color:var(--white);padding:30px 34px 0 34px}
  .provide .section-title{font-size:27px;font-weight:400}
  .provide-head{font-family:"Tinos",serif;font-weight:700;font-size:16.5px;color:var(--orange);margin:14px 0 8px}
  .provide .svc-list li{font-size:13px}

  /* process */
  .process{position:absolute;left:0;top:852px;width:912px;height:172px;background:var(--navy)}
  .process h2{position:absolute;left:48px;top:22px;font-family:"Tinos",serif;font-weight:700;font-size:27px;color:var(--white)}
  .steps{position:absolute;left:20px;top:76px;display:flex;align-items:center}
  .step{width:206px;height:70px;border-radius:18px;display:flex;align-items:center;padding-left:34px;font-family:"Roboto",Arial,sans-serif;font-weight:500;font-size:18px;line-height:21px;color:var(--white);margin-right:-14px}
  .step:nth-child(1){background:var(--blue-light)}
  .step:nth-child(3){background:var(--blue-mid)}
  .step:nth-child(5){background:#3a6ab8}
  .step:nth-child(7){background:var(--blue-deep);width:230px;margin-right:0}
  .arrow{position:relative;z-index:2;width:30px;height:30px;margin:0 -2px 0 -16px}
  .arrow + .step{padding-left:36px}

  /* footer */
  .footer{position:absolute;left:0;top:1024px;width:912px;height:156px;background:var(--white)}
  .brand{position:absolute;left:60px;top:48px;display:flex;align-items:center;gap:14px}
  .brand-dot{width:34px;height:34px;border-radius:50%;background:var(--orange)}
  .brand-name{font-family:"Lato",Arial,sans-serif;font-weight:700;font-size:30px;letter-spacing:4px;color:var(--navy);line-height:32px}
  .contact{position:absolute;right:48px;top:22px;text-align:right}
  .phone{font-family:"Roboto",Arial,sans-serif;font-weight:500;font-size:68px;line-height:74px;color:var(--orange);letter-spacing:1px}
  .links{font-size:16px;font-weight:700;color:var(--ink)}
  .links a{color:var(--ink);text-decoration:none}
</style>
</head>
<body>
<main class="flyer">
  <header class="hero">
    <svg width="912" height="250" viewBox="0 0 912 250" aria-hidden="true">
      <path d="M0,0 H912 V150 Q560,250 0,226 Z" fill="#0f1b3d"/>
      <path d="M0,234 Q560,258 912,158" fill="none" stroke="#f37122" stroke-width="5"/>
    </svg>
    <h1>Regulatory support for medtech firms.<br>Diligence for investors.</h1>
  </header>

  <section class="experience">
    <h2 class="section-title">EXPERIENCE:</h2>
    <ul class="bullets">
      <li>Over a decade @FDA (Former Deputy Division Director)</li>
      <li>Expertise: Cardiovascular, Ophthalmology, General Hospital, Infection Control, Dental, Anesthesia, Respiratory</li>
      <li>Vice President Regulatory Affairs / Quality Assurance @Corvane (Fortune 150 Company)</li>
      <li class="tight gap">Initiated reorganization of department</li>
      <li class="tight">Led major compliance effort</li>
      <li class="tight">Successful FDA inspection (no observations)</li>
    </ul>
  </section>

  <svg class="venn" viewBox="0 0 340 300" role="img" aria-label="Diagram: Experience, Network and Process overlap to create Leverage">
    <defs>
      <linearGradient id="grey" x1="0" y1="0" x2="0" y2="1">
        <stop offset="0" stop-color="#7f8187"/>
        <stop offset="1" stop-color="#d8d9dc"/>
      </linearGradient>
    </defs>
    <circle cx="100" cy="110" r="78" fill="url(#grey)" stroke="#8fd3a9" stroke-width="1.5"/>
    <circle cx="238" cy="96" r="78" fill="url(#grey)" stroke="#8fd3a9" stroke-width="1.5"/>
    <circle cx="186" cy="196" r="78" fill="url(#grey)" stroke="#8fd3a9" stroke-width="1.5"/>
    <circle cx="170" cy="126" r="40" fill="#0f1b3d"/>
    <text x="74" y="114">Experience</text>
    <text x="262" y="96">Network</text>
    <text x="196" y="226">Process</text>
    <text x="170" y="131">Leverage</text>
  </svg>

  <section class="services">
    <h2 class="section-title">SERVICES:</h2>
    <div class="svc-cols">
      <div class="svc-col">
        <h3 class="svc-head">Regulatory Strategy</h3>
        <ul class="svc-list">
          <li>RAQA Organizational Structure</li>
          <li>Regulatory Pathway</li>
        </ul>
        <h3 class="svc-head">Interim Executive Leadership</h3>
        <ul class="svc-list">
          <li>Compliance Remediation</li>
          <li>Accelerated Product Registration</li>
        </ul>
      </div>
      <div class="svc-col">
        <h3 class="svc-head">FDA Communications</h3>
        <ul class="svc-list">
          <li>Deficiency Response</li>
          <li>Application Review</li>
        </ul>
        <h3 class="svc-head">Training</h3>
        <ul class="svc-list">
          <li>FDA Communication</li>
          <li>MDR Reporting</li>
        </ul>
      </div>
    </div>
  </section>

  <section class="provide">
    <h2 class="section-title">Experience to Provide...</h2>
    <h3 class="provide-head">Executive Application Review</h3>
    <ul class="svc-list">
      <li>Examples include: Presubmission, IDE, 510(k), 513(g), PMA, Refuse to Accept, Hold letter</li>
      <li>Troubleshooting</li>
    </ul>
    <h3 class="provide-head">Strategic Advice &amp; Diligence to Investors</h3>
    <ul class="svc-list">
      <li>Validate &amp; Verify Founder Milestones</li>
      <li>Diligence portfolio company Regulatory and Quality systems</li>
    </ul>
  </section>

  <section class="process">
    <h2>Efficient Process</h2>
    <div class="steps">
      <div class="step">Exploratory<br>Call</div>
      <svg class="arrow" viewBox="0 0 30 30" aria-hidden="true"><circle cx="15" cy="15" r="13" fill="#fff"/><path d="M8 15h12M15 10l5 5-5 5" stroke="#2f63bb" stroke-width="2.6" fill="none" stroke-linecap="round" stroke-linejoin="round"/></svg>
      <div class="step">Regulatory<br>Landscape</div>
      <svg class="arrow" viewBox="0 0 30 30" aria-hidden="true"><circle cx="15" cy="15" r="13" fill="#fff"/><path d="M8 15h12M15 10l5 5-5 5" stroke="#2f63bb" stroke-width="2.6" fill="none" stroke-linecap="round" stroke-linejoin="round"/></svg>
      <div class="step">Problem<br>Statement</div>
      <svg class="arrow" viewBox="0 0 30 30" aria-hidden="true"><circle cx="15" cy="15" r="13" fill="#fff"/><path d="M8 15h12M15 10l5 5-5 5" stroke="#2f63bb" stroke-width="2.6" fill="none" stroke-linecap="round" stroke-linejoin="round"/></svg>
      <div class="step">Review &amp; Align on<br>Deliverables</div>
    </div>
  </section>

  <footer class="footer">
    <div class="brand">
      <span class="brand-dot"></span>
      <span class="brand-name">HALDEN<br>ADVISORY</span>
    </div>
    <div class="contact">
      <div class="phone">555.014.2280</div>
      <div class="links"><a href="mailto:info@haldenadvisory.com">info@haldenadvisory.com</a> | <a href="https://www.haldenadvisory.com">www.haldenadvisory.com</a></div>
    </div>
  </footer>
</main>
</body>
</html>
```